Chocolate Drink In Velo Karn 250ml

We need to design our Chocolate Drink in Velo Folde. We already have a logo attached. This product is a Whole Chocolate Milk 8oz (236ml). Our target customers are kids, young adults & adults young at heart. We will be selling this in the U.S.. The design should be simple, attractive and good mixed of colors that will get the attention of everyone especially to the kids.

Packaging template is attached

Target Market(s)

Our target markets are kids, young adults and adults young at heart. We will be selling this product in the U.S.

Industry/Entity Type

Grocery Store

Font styles to use
Other font styles liked:
• comic sans

Requirements
Must have
• My project must have a design that will attract kids and young adults.
Nice to have
• I would like to see simple attractive colors and caricature that will be attractive to the kids.

```html
<!DOCTYPE html>
<html lang="en">
<head>
<meta charset="UTF-8">
<title>Moca-Zun Whole Chocolate Milk – Carton Front</title>
<link rel="stylesheet" href="https://fonts.googleapis.com/css2?family=Indie+Flower&display=swap">
<style>
  :root {
    --stage: #eef0f2;
    --carton: #ffffff;
    --carton-edge: #dfe3e7;
    --brand-blue: #1f4f86;
    --calcium-blue: #3a6fb3;
    --whole-pink: #e0407a;
    --chocolate-orange: #f0891e;
    --milk-blue: #3563b0;
    --size-orange: #f29a2e;
    --cocoa: #4a2414;
    --cocoa-soft: #8a5a44;
    --cream: #f4efe9;
  }
  * { box-sizing: border-box; margin: 0; padding: 0; }
  html, body {
    width: 1200px;
    height: 1067px;
    overflow: hidden;
    background: var(--stage);
  }
  .canvas {
    position: relative;
    width: 1200px;
    height: 1067px;
    display: flex;
    align-items: center;
    justify-content: center;
  }
  .carton-front {
    position: relative;
    width: 560px;
    height: 960px;
    background: var(--carton);
    border: 2px solid var(--carton-edge);
    border-radius: 14px;
    display: flex;
    flex-direction: column;
    align-items: center;
    font-family: "Indie Flower", "Comic Sans MS", cursive;
  }
  .brand-mark {
    margin-top: 90px;
    display: flex;
    align-items: center;
    gap: 14px;
  }
  .brand-mark__dot {
    width: 22px;
    height: 22px;
    border-radius: 50%;
    background: var(--brand-blue);
  }
  .brand-mark__name {
    font-size: 52px;
    font-weight: 400;
    color: var(--brand-blue);
    letter-spacing: 2px;
  }
  .calcium-claim {
    margin-top: 70px;
    text-align: center;
    color: var(--calcium-blue);
    line-height: 1.05;
  }
  .calcium-claim__lead { display: block; font-size: 32px; }
  .calcium-claim__main { display: block; font-size: 46px; }
  .product-name {
    position: relative;
    margin-top: 50px;
    width: 420px;
    height: 420px;
    display: flex;
    align-items: center;
    justify-content: center;
  }
  .product-name__splash {
    position: absolute;
    inset: 0;
    border-radius: 50%;
    background: radial-gradient(circle at 50% 50%,
      var(--carton) 0 52%,
      var(--cream) 60%,
      var(--cocoa-soft) 70%,
      var(--cocoa) 78%,
      var(--cream) 90%,
      var(--carton) 100%);
    opacity: 0.9;
  }
  .product-name__text {
    position: relative;
    text-align: center;
    line-height: 1;
  }
  .product-name__whole { display: block; font-size: 74px; color: var(--whole-pink); }
  .product-name__chocolate { display: block; font-size: 74px; color: var(--chocolate-orange); }
  .product-name__milk { display: block; font-size: 74px; color: var(--milk-blue); }
  .net-volume {
    margin-top: 70px;
    font-size: 44px;
    color: var(--size-orange);
    letter-spacing: 1px;
  }
</style>
</head>
<body>
  <main class="canvas">
    <section class="carton-front">
      <div class="brand-mark">
        <span class="brand-mark__dot"></span>
        <span class="brand-mark__name">MOCA-ZUN</span>
      </div>

      <p class="calcium-claim">
        <span class="calcium-claim__lead">an excellent source</span>
        <span class="calcium-claim__main">of Calcium</span>
      </p>

      <div class="product-name">
        <div class="product-name__splash" role="img" aria-label="Ring of splashing dark chocolate and white milk"></div>
        <h1 class="product-name__text">
          <span class="product-name__whole">Whole</span>
          <span class="product-name__chocolate">Chocolate</span>
          <span class="product-name__milk">Milk</span>
        </h1>
      </div>

      <p class="net-volume">8oz (236ml)</p>
    </section>
  </main>
</body>
</html>
```